Design a CD Cover For Baby Music and Lullabies To Appear on Tune Harbor Shop etc.

Please read this brief before you design. Otherwise you will be wasting your time.

I need a cd cover for music albums which will appear on streaming sites such as Tune Harbor Shop Wavelane, Pluvix etc. for the brand Cozy Cradle Tunes. The thumbnails are quite small so the text needs to be quite large.

I need a design if possible, in which I can simply alter the title of the album and the baby picture so that each album has a different cover but works with the branding.

You can check out the Cozy Cradle Tunes on the Tune Harbor shop.
https://play.wavelane.example/artist/7qk3RtLmWvNx82hYbPdaZe

I made those covers and I really don't like them at all! As you can tell I am not a graphic designer. Ha.

Please help me with a modern, eye catching and cute design that will work across the brand now and in the future. The CCT logo and the name Cozy Cradle Tunes is the only thing that needs to be used somewhere in the design.

Please use the title

Soft Hush Tones For Nap Time Part First

for this first album.
(White noise sounds are hair dryers, vacuum cleaners, fans, wind, rain, the sea, white noise, pink noise, brown noise etc. )

Here is an example of album covers which are coherent. A style like this without the over the top text would be good. But don't copy these!
https://play.wavelane.example/artist/9TfKxcMnEuGh31oAsQbiR5

Target Market(s)

Parents of babies.

Font styles to use
Serif
Sans Serif

Colors

Designer to choose colors to be used in the design.

Requirements
Must have
• Large font so it can been seen in the wavelane thumbnail. A photo of a baby. Please take a look at the wavelane and tune harbor stores. The Cozy Cradle Tunes logo.
• Album Title
• Soft Hush Tones For Nap Time Part First

```html
<!DOCTYPE html>
<html lang="en">
<head>
<meta charset="utf-8">
<title>Soft Hush Tones For Nap Time – Part First</title>
<link rel="stylesheet" href="https://fonts.googleapis.com/css2?family=Josefin+Sans:wght@600;700&family=Great+Vibes&display=swap">
<style>
  :root {
    --navy-deep: #001c58;
    --navy: #0b2a6e;
    --band-light: #a9e4fc;
    --band-mid: #5cc9f4;
    --title-blue: #8fd3fb;
    --script-white: #f7f7f7;
    --photo-teal: #1a8f9c;
    --photo-blue: #2c6fd6;
    --photo-skin: #c98f7f;
  }
  html, body {
    margin: 0;
    padding: 0;
    width: 1200px;
    height: 1200px;
    overflow: hidden;
    background: var(--navy-deep);
  }
  .album-cover {
    position: relative;
    width: 1200px;
    height: 1200px;
  }
  .cover-art {
    position: absolute;
    inset: 0;
    width: 1200px;
    height: 1200px;
    display: block;
  }
  .title-caps {
    font-family: "Josefin Sans", sans-serif;
    font-weight: 700;
    fill: var(--title-blue);
  }
  .title-sub {
    font-family: "Josefin Sans", sans-serif;
    font-weight: 700;
    fill: var(--script-white);
  }
  .title-script {
    font-family: "Great Vibes", cursive;
    fill: var(--script-white);
  }
  .title-part {
    font-family: "Josefin Sans", sans-serif;
    font-weight: 600;
    fill: var(--title-blue);
  }
  .brand-name {
    font-family: "Josefin Sans", sans-serif;
    font-weight: 700;
    fill: var(--title-blue);
  }
  .text-shadow { filter: url(#soft-drop); }
</style>
</head>
<body>
<main class="album-cover">
  <svg class="cover-art" viewBox="0 0 1200 1200" xmlns="http://www.w3.org/2000/svg">
    <defs>
      <linearGradient id="navy-field" x1="0" y1="0" x2="0" y2="1">
        <stop offset="0" stop-color="var(--navy)"/>
        <stop offset="1" stop-color="var(--navy-deep)"/>
      </linearGradient>
      <radialGradient id="photo-tones" cx="0.62" cy="0.55" r="0.7">
        <stop offset="0" stop-color="var(--photo-skin)"/>
        <stop offset="0.35" stop-color="var(--photo-blue)"/>
        <stop offset="1" stop-color="var(--photo-teal)"/>
      </radialGradient>
      <filter id="soft-drop" x="-10%" y="-10%" width="120%" height="130%">
        <feDropShadow dx="3" dy="5" stdDeviation="4" flood-color="#000" flood-opacity="0.45"/>
      </filter>
      <filter id="band-shadow" x="-10%" y="-10%" width="130%" height="130%">
        <feDropShadow dx="6" dy="6" stdDeviation="8" flood-color="#000" flood-opacity="0.35"/>
      </filter>
    </defs>

    <rect class="navy-field" width="1200" height="1200" fill="url(#navy-field)"/>

    <path class="wave-band wave-band--mid" filter="url(#band-shadow)" fill="var(--band-mid)"
      d="M752 0 C700 120 560 300 610 520 C650 700 570 830 390 875 C210 915 80 1080 0 1200 L0 0 Z"/>
    <path class="wave-band wave-band--light" filter="url(#band-shadow)" fill="var(--band-light)"
      d="M672 0 C640 130 520 280 568 480 C610 660 560 800 420 845 C250 900 110 1040 0 1180 L0 0 Z"/>

    <path class="baby-photo" role="img" aria-label="Photo of a sleeping newborn in a blue flower bonnet, wrapped in a teal knit blanket"
      filter="url(#band-shadow)" fill="url(#photo-tones)"
      d="M590 0 C592 120 482 250 522 420 C562 560 600 700 500 815 C390 880 230 960 60 1140 L0 1190 L0 0 Z"/>

    <g class="brand-mark">
      <circle cx="1075" cy="135" r="46" fill="var(--band-mid)"/>
      <text class="brand-name" x="1012" y="144" font-size="26" text-anchor="end">COZY CRADLE TUNES</text>
    </g>

    <g class="album-title text-shadow">
      <text class="title-caps" x="1142" y="528" font-size="158" text-anchor="end">SOFT</text>
      <text class="title-caps" x="1142" y="725" font-size="158" text-anchor="end">HUSH</text>
      <text class="title-sub" x="1137" y="812" font-size="54" text-anchor="end">TONES FOR</text>
      <text class="title-script" x="1160" y="974" font-size="168" text-anchor="end">Nap Time</text>
      <text class="title-part" x="1140" y="1100" font-size="62" text-anchor="end">PART. FIRST</text>
    </g>
  </svg>
</main>
</body>
</html>
```